Velmora Powerpoint Templates

Create a Powerpoint Template based on existing logo, colors, mascot with support for the 10-12 most important slides types, default format FullHD re ...

Target Market(s)

Thailand

Industry/Entity Type

Insurance Broker

Font styles to use
Sans Serif

```html
<!DOCTYPE html>
<html lang="en">
<head>
<meta charset="utf-8">
<title>Velmora Presentation Template</title>
<link href="https://fonts.googleapis.com/css2?family=Open+Sans:wght@400;600;700&display=swap" rel="stylesheet">
<style>
:root{
  --yellow:#fcc95b;
  --blue:#3a99d2;
  --dark:#4b4b4b;
  --ink:#333;
  --muted:#777;
  --sheet:#e6e6e6;
  --white:#fff;
  --tan:#c9a45a;
}
*{margin:0;padding:0;box-sizing:border-box}
html,body{width:1200px;height:927px;overflow:hidden;background:var(--sheet);font-family:'Open Sans',Arial,sans-serif;color:var(--ink)}
.deck{position:relative;width:1200px;height:927px}
.slide{position:absolute;width:380px;height:214px;background:var(--white);overflow:hidden}
.c1{left:18px}.c2{left:412px}.c3{left:806px}
.r1{top:18px}.r2{top:244px}.r3{top:470px}.r4{top:695px}
.abs{position:absolute}
.footer-bar{position:absolute;left:0;right:0;bottom:0;height:8px;background:var(--blue)}
.page-num{position:absolute;right:6px;bottom:0;font-size:5px;line-height:8px;color:var(--white)}
.brand-tag{position:absolute;right:10px;top:6px;display:flex;align-items:center;gap:2px;font-size:9px;font-weight:600;color:var(--yellow)}
.brand-tag i{width:5px;height:5px;border-radius:50%;background:var(--dark);display:block}
.slide-title{position:absolute;font-size:14.5px;font-weight:600;color:var(--ink);white-space:nowrap}
.center-x{left:0;right:0;text-align:center}
.body-text{font-size:5.4px;line-height:1.45;color:var(--ink);text-align:justify}
.placeholder{position:absolute}
.dot{position:absolute;border-radius:50%}
.small-head{font-weight:700;font-size:5.4px}

/* slide 1 */
.title-slide{background:var(--yellow)}
.title-panel{position:absolute;left:17px;top:14px;width:349px;height:186px;background:linear-gradient(135deg,#4a4f58,#2c2f35 55%,#555a62);clip-path:polygon(0 0,72% 0,78% 9%,100% 9%,100% 100%,14% 100%,8% 91%,0 91%)}
.title-brand{position:absolute;top:40px;left:0;right:0;text-align:center;font-size:32px;font-weight:600;color:var(--yellow);letter-spacing:.5px}
.title-main{position:absolute;top:122px;left:0;right:0;text-align:center;font-size:22px;font-weight:700;color:var(--white)}
.title-sub{position:absolute;top:150px;left:0;right:0;text-align:center;font-size:10px;color:var(--white)}

/* section */
.photo-fill{position:absolute;inset:0;background:linear-gradient(160deg,#8a4a45,#5d4c55 35%,#2f3a44 70%,#1c2229)}
.section-band{position:absolute;left:100px;right:0;top:68px;height:74px;background:rgba(58,153,210,.85)}
.section-num{position:absolute;left:13px;top:18px;font-size:32px;font-weight:700;color:var(--white);line-height:1}
.section-rule{position:absolute;left:65px;top:15px;width:1px;height:46px;background:var(--white)}
.section-title{position:absolute;left:73px;top:14px;font-size:12.5px;line-height:1.3;color:var(--white)}
.section-sub{position:absolute;left:73px;top:54px;font-size:4.5px;color:var(--white)}

/* numbered list */
.num-frame{position:absolute;left:229px;top:47px;width:131px;height:143px;border:2px solid var(--yellow)}
.num-badge{position:absolute;width:17px;height:17px;border-radius:50%;border:2px solid var(--yellow);background:var(--white);font-size:6.5px;font-weight:700;display:flex;align-items:center;justify-content:center}
.num-item{position:absolute;left:244px;width:110px}
.num-item b{display:block;font-size:5px;font-weight:600}
.num-item p{font-size:4.2px;line-height:1.35;color:var(--ink)}

/* checklist */
.check-item{position:absolute;left:25px;width:175px;display:flex;gap:7px}
.check-icon{flex:0 0 13px;height:13px}
.check-item p{font-size:4.2px;line-height:1.4}
.quote-box{position:absolute;left:208px;top:110px;right:0;bottom:8px;background:var(--blue);color:var(--white);text-align:center}
.quote-mark{font-size:34px;font-weight:700;line-height:1;margin-top:0;height:26px}
.quote-box p{font-size:6.4px;line-height:1.3;padding:0 42px}

/* icon rows */
.icon-row{position:absolute;left:31px;display:flex;align-items:center;gap:10px}
.round-icon{width:27px;height:27px;border-radius:50%;display:flex;align-items:center;justify-content:center}
.icon-row p{width:100px;font-size:4.4px;line-height:1.4}

/* comparison */
.col-label{position:absolute;top:44px;font-size:6px;font-weight:600}
.col-rule{position:absolute;top:55px;height:1px;background:#ddd}
.cmp-item{position:absolute;display:flex;align-items:center;gap:8px;font-size:6.4px;color:var(--muted)}
.cmp-mark{width:17px;height:17px;border-radius:50%;border:1px solid #e3e3e3;display:flex;align-items:center;justify-content:center}

/* quote slide */
.quote-band{position:absolute;left:0;right:0;top:50px;height:97px;background:var(--yellow)}
.quote-frame{position:absolute;left:78px;top:26px;width:226px;height:145px;border:2px solid var(--blue)}
.quote-text{position:absolute;left:110px;top:72px;width:160px;text-align:center;font-size:8.5px;line-height:1.5;color:var(--white)}
.quote-cite{position:absolute;right:86px;top:135px;font-size:6.4px;color:var(--white)}

/* stats slide */
.stat-circle{position:absolute;left:229px;top:56px;width:108px;height:108px;border-radius:50%;background:var(--yellow);color:var(--white);text-align:center}
.stat-circle strong{display:block;margin-top:32px;font-size:27px;line-height:1}
.stat-circle span{font-size:8.5px}
.info-strip{position:absolute;left:3px;top:158px;width:187px;height:40px;background:#f2f2f2;display:flex;align-items:center;gap:4px;padding:0 6px}
.info-strip .round-icon{width:18px;height:18px;flex:0 0 18px}
.info-strip p{font-size:3.8px;line-height:1.35;width:62px}
.info-strip b{color:var(--blue);font-weight:600}

/* contact */
.contact-bubble{position:absolute;left:29px;top:54px;width:125px;height:104px;border-radius:14px;background:var(--dark);color:var(--white);text-align:center}
.contact-bubble h3{font-size:15.5px;font-weight:600;margin-top:20px}
.contact-bubble p{font-size:4.4px;line-height:1.35;padding:2px 12px 0}
.contact-tail{position:absolute;left:153px;top:113px}
.person-name{position:absolute;left:193px;top:39px;font-size:13.5px;font-weight:600;color:var(--blue)}
.person-role{position:absolute;left:193px;top:57px;font-size:8.5px;color:var(--yellow)}
.contact-line{position:absolute;left:187px;display:flex;align-items:center;gap:10px;font-size:7.5px;color:var(--ink)}
.contact-line .round-icon{width:20px;height:20px;border:1px solid #e5e5e5;background:var(--white)}
.tagline{position:absolute;left:0;right:0;top:183px;text-align:center;font-size:11.5px;font-weight:600;color:var(--blue)}
</style>
</head>
<body>
<main class="deck">

  <!-- 1 Title -->
  <section class="slide c1 r1 title-slide">
    <div class="title-panel" role="img" aria-label="Photo of two toy cars parked on stacks of coins"></div>
    <div class="title-brand">Velmora</div>
    <div class="title-main">Your Slides Deck Name</div>
    <div class="title-sub">Your Slides Deck Name</div>
    <span class="page-num" style="color:#fff;bottom:2px">2</span>
  </section>

  <!-- 2 Mascot intro -->
  <section class="slide c2 r1">
    <div class="slide-title" style="left:107px;top:22px">Lorem ipsum dolor eta</div>
    <div class="brand-tag"><i></i>Velmora</div>
    <div class="placeholder" style="left:6px;top:48px;width:124px;height:130px;background:radial-gradient(circle at 55% 45%,#5aaee0,#3a99d2 55%,#e9f3fa 75%,transparent 76%)" role="img" aria-label="Brand mascot character in blue mask and cape presenting"></div>
    <p class="abs body-text" style="left:162px;top:66px;width:196px">Lorem ipsum dolor sit amet, consectetur adipiscing elit, sed do eiusmod tempor incididunt ut labore et dolore magna aliqua. Ut enim ad minim veniam, quis nostrud exercitation ullamco laboris nisi ut aliquip ex</p>
    <div class="abs" style="left:162px;top:110px;right:0;height:38px;background:var(--yellow)"></div>
    <p class="abs body-text" style="left:168px;top:119px;width:190px">Lorem ipsum dolor sit amet, consectetur adipiscing elit, sed do eiusmod tempor incididunt ut labore et dolore magna aliqua. Ut enim ad minim veniam, quis nostrud exercitation ullamco laboris nisi ut aliquip ex</p>
    <p class="abs body-text" style="left:162px;top:170px;width:196px">Lorem ipsum dolor sit amet, consectetur adipiscing elit, sed do eiusmod tempor incididunt ut labore et dolore magna aliqua. Ut enim ad minim veniam, quis nostrud exercitation ullamco laboris nisi ut aliquip ex</p>
    <div class="footer-bar"></div><span class="page-num">3</span>
  </section>

  <!-- 3 Numbered list -->
  <section class="slide c3 r1">
    <div class="slide-title" style="left:107px;top:22px">Lorem ipsum dolor eta</div>
    <div class="brand-tag"><i></i>Velmora</div>
    <div class="abs" style="left:0;top:63px;width:18px;height:95px;background:var(--yellow)"></div>
    <p class="abs body-text" style="left:29px;top:66px;width:171px;font-size:4.6px">Sed ut perspiciatis, unde omnis iste natus error sit voluptatem accusantium doloremque laudantium, totam rem aperiam eaque ipsa, quae ab illo inventore veritatis et quasi architecto beatae vitae dicta sunt, explicabo. <b>Nemo enim ipsam voluptatem</b>, quia voluptas sit, aspernatur aut odit aut fugit, sed quia consequuntur magni dolores eos, qui ratione <b>voluptatem sequi nesciunt</b>, neque porro quisquam est. Sed ut perspiciatis, unde omnis iste natus error sit voluptatem accusantium doloremque laudantium, totam rem aperiam eaque ipsa, quae ab illo inventore veritatis et quasi architecto beatae vitae dicta sunt, explicabo. <b>Nemo enim ipsam voluptatem</b>, quia voluptas sit, aspernatur aut odit aut fugit.</p>
    <div class="num-frame"></div>
    <div class="num-badge" style="left:220px;top:58px">01</div>
    <div class="num-badge" style="left:220px;top:91px">02</div>
    <div class="num-badge" style="left:220px;top:125px">03</div>
    <div class="num-badge" style="left:220px;top:158px">04</div>
    <div class="num-item" style="top:53px"><b>Your Text Here</b><p>Lorem ipsum dolor sit amet, consectetur adipiscing elit, sed do eiusmod tempor incididunt ut labore et dolore magna aliqua.</p></div>
    <div class="num-item" style="top:87px"><b>Your Text Here</b><p>Lorem ipsum dolor sit amet, consectetur adipiscing elit, sed do eiusmod tempor incididunt ut labore et dolore magna aliqua.</p></div>
    <div class="num-item" style="top:120px"><b>Your Text Here</b><p>Lorem ipsum dolor sit amet, consectetur adipiscing elit, sed do eiusmod tempor incididunt ut labore et dolore magna aliqua.</p></div>
    <div class="num-item" style="top:153px"><b>Your Text Here</b><p>Lorem ipsum dolor sit amet, consectetur adipiscing elit, sed do eiusmod tempor incididunt ut labore et dolore magna aliqua.</p></div>
    <div class="footer-bar"></div><span class="page-num">4</span>
  </section>

  <!-- 4 Section -->
  <section class="slide c1 r2">
    <div class="photo-fill" role="img" aria-label="Photo of rows of new cars in a parking lot at sunset"></div>
    <div class="section-band">
      <div class="section-num">01</div>
      <div class="section-rule"></div>
      <div class="section-title">THE<br>COMPANY</div>
      <div class="section-sub">This is the subtitle that makes it comprehensible</div>
    </div>
    <span class="page-num" style="bottom:2px">5</span>
  </section>

  <!-- 5 Checklist with quote -->
  <section class="slide c2 r2">
    <div class="slide-title" style="left:26px;top:26px">Lorem ipsum dolor eta</div>
    <div class="check-item" style="top:56px">
      <svg class="check-icon" viewBox="0 0 14 14"><circle cx="7" cy="7" r="7" fill="#3a99d2"/><path d="M3.8 7.2l2.2 2.2 4.2-4.4" stroke="#fff" stroke-width="1.4" fill="none"/></svg>
      <p><span class="small-head">Lorem ipsum dolor</span><br>Lorem ipsum dolor sit amet, on met consectetur elota adipiscing elit, sed do eiusmod tempor karamtam o kad mel etolik esti emka et.</p>
    </div>
    <div class="check-item" style="top:99px">
      <svg class="check-icon" viewBox="0 0 14 14"><circle cx="7" cy="7" r="7" fill="#3a99d2"/><path d="M3.8 7.2l2.2 2.2 4.2-4.4" stroke="#fff" stroke-width="1.4" fill="none"/></svg>
      <p><span class="small-head">Lorem ipsum dolor</span><br>Lorem ipsum dolor sit amet, on met consectetur elota adipiscing elit, sed do eiusmod tempor karamtam o kad mel etolik esti emka et.</p>
    </div>
    <div class="check-item" style="top:142px">
      <svg class="check-icon" viewBox="0 0 14 14"><circle cx="7" cy="7" r="7" fill="#3a99d2"/><path d="M3.8 7.2l2.2 2.2 4.2-4.4" stroke="#fff" stroke-width="1.4" fill="none"/></svg>
      <p><span class="small-head">Lorem ipsum dolor</span><br>Lorem ipsum dolor sit amet, on met consectetur elota adipiscing elit, sed do eiusmod tempor karamtam o kad mel etolik esti emka et.</p>
    </div>
    <div class="placeholder" style="left:226px;top:4px;width:94px;height:104px;background:radial-gradient(circle at 50% 45%,#5aaee0,#3a99d2 50%,#e9f3fa 72%,transparent 73%)" role="img" aria-label="Brand mascot character holding out a coin"></div>
    <div class="dot" style="left:323px;top:22px;width:48px;height:48px;background:var(--dark);border:5px solid #8a8a8a"></div>
    <div class="dot" style="left:332px;top:31px;width:30px;height:30px;background:var(--yellow)"></div>
    <div class="quote-box">
      <div class="quote-mark">&ldquo;</div>
      <p>Lorem ipsum dolor sit amet, consectetur adipiscing elit, sed do eiusmod tempor incididunt ut labore et dolore magna aliqua.</p>
    </div>
    <div class="footer-bar"></div><span class="page-num">6</span>
  </section>

  <!-- 6 Cycle -->
  <section class="slide c3 r2">
    <div class="slide-title" style="left:108px;top:19px">Lorem ipsum dolor eta</div>
    <div class="brand-tag"><i></i>Velmora</div>
    <div class="icon-row" style="top:60px">
      <div class="round-icon" style="background:var(--blue)"><svg width="12" height="12" viewBox="0 0 12 12"><circle cx="6" cy="5" r="3" fill="#fff"/><rect x="4.8" y="8" width="2.4" height="2.5" fill="#fff"/></svg></div>
      <p>Lorem ipsum dolor sit amet, consectetur adipiscing elit, sed do eiusmod tempor incididunt ut labore et dolore magna aliqua.</p>
    </div>
    <div class="icon-row" style="top:100px">
      <div class="round-icon" style="background:var(--yellow)"><svg width="12" height="12" viewBox="0 0 12 12"><rect x="2" y="2.5" width="8" height="7.5" fill="none" stroke="#fff" stroke-width="1.2"/><path d="M2 5h8" stroke="#fff"/></svg></div>
      <p>Lorem ipsum dolor sit amet, consectetur adipiscing elit, sed do eiusmod tempor incididunt ut labore et dolore magna aliqua.</p>
    </div>
    <div class="icon-row" style="top:143px">
      <div class="round-icon" style="background:var(--dark)"><svg width="12" height="12" viewBox="0 0 12 12"><path d="M2 7l5-5h3v3l-5 5z" fill="#fff"/><circle cx="8.3" cy="3.7" r=".9" fill="#4b4b4b"/></svg></div>
      <p>Lorem ipsum dolor sit amet, consectetur adipiscing elit, sed do eiusmod tempor incididunt ut labore et dolore magna aliqua.</p>
    </div>
    <svg class="abs" style="left:218px;top:52px" width="122" height="122" viewBox="0 0 122 122">
      <g fill="none" stroke-width="30" transform="rotate(165 61 61)">
        <circle cx="61" cy="61" r="45" stroke="#3a99d2" stroke-dasharray="98 185"/>
        <circle cx="61" cy="61" r="45" stroke="#fcc95b" stroke-dasharray="88 195" stroke-dashoffset="-102"/>
        <circle cx="61" cy="61" r="45" stroke="#4b4b4b" stroke-dasharray="86 197" stroke-dashoffset="-194"/>
      </g>
      <circle cx="37" cy="38" r="3.5" fill="#fff"/>
      <rect x="86" y="43" width="8" height="8" fill="none" stroke="#fff"/>
      <path d="M45 94l6-6h4v4l-6 6z" fill="#fff"/>
    </svg>
    <div class="footer-bar"></div><span class="page-num">7</span>
  </section>

  <!-- 7 Comparison -->
  <section class="slide c1 r3">
    <div class="slide-title" style="left:0;right:0;text-align:center;top:20px;font-size:16px">Comparison</div>
    <div class="brand-tag"><i></i>Velmora</div>
    <div class="col-label" style="left:27px;color:var(--blue)">DO'S</div>
    <div class="col-rule" style="left:27px;width:165px"></div>
    <div class="col-label" style="right:30px;color:var(--yellow)">DON'TS</div>
    <div class="col-rule" style="right:30px;width:145px"></div>
    <div class="cmp-item" style="left:27px;top:82px">This is a sample text.<span class="cmp-mark"><svg width="8" height="8" viewBox="0 0 8 8"><path d="M1 4l2 2 4-4" stroke="#3a99d2" fill="none"/></svg></span></div>
    <div class="cmp-item" style="left:27px;top:108px">This is a sample text.<span class="cmp-mark"><svg width="8" height="8" viewBox="0 0 8 8"><path d="M1 4l2 2 4-4" stroke="#3a99d2" fill="none"/></svg></span></div>
    <div class="cmp-item" style="left:27px;top:134px">This is a sample text.<span class="cmp-mark"><svg width="8" height="8" viewBox="0 0 8 8"><path d="M1 4l2 2 4-4" stroke="#3a99d2" fill="none"/></svg></span></div>
    <div class="cmp-item" style="left:27px;top:160px">This is a sample text.<span class="cmp-mark"><svg width="8" height="8" viewBox="0 0 8 8"><path d="M1 4l2 2 4-4" stroke="#3a99d2" fill="none"/></svg></span></div>
    <div class="cmp-item" style="left:256px;top:81px"><span class="cmp-mark"><svg width="7" height="7" viewBox="0 0 7 7"><path d="M1 1l5 5M6 1l-5 5" stroke="#fcc95b"/></svg></span>This is a sample text.</div>
    <div class="cmp-item" style="left:256px;top:107px"><span class="cmp-mark"><svg width="7" height="7" viewBox="0 0 7 7"><path d="M1 1l5 5M6 1l-5 5" stroke="#fcc95b"/></svg></span>This is a sample text.</div>
    <div class="cmp-item" style="left:256px;top:133px"><span class="cmp-mark"><svg width="7" height="7" viewBox="0 0 7 7"><path d="M1 1l5 5M6 1l-5 5" stroke="#fcc95b"/></svg></span>This is a sample text.</div>
    <div class="cmp-item" style="left:256px;top:159px"><span class="cmp-mark"><svg width="7" height="7" viewBox="0 0 7 7"><path d="M1 1l5 5M6 1l-5 5" stroke="#fcc95b"/></svg></span>This is a sample text.</div>
    <svg class="abs" style="left:142px;top:80px" width="96" height="96" viewBox="0 0 96 96">
      <path d="M47 0A48 48 0 0 0 47 96z" fill="#3a99d2"/>
      <path d="M49 0A48 48 0 0 1 49 96z" fill="#fcc95b"/>
      <path d="M16 58v-14h5l5-10c2 0 3 1 3 3l-1 6h7c2 0 3 2 2 4l-3 9c0 2-2 2-3 2H21z" fill="none" stroke="#fff" stroke-width="1.5"/>
      <path d="M80 38v14h-5l-5 10c-2 0-3-1-3-3l1-6h-7c-2 0-3-2-2-4l3-9c0-2 2-2 3-2h10z" fill="none" stroke="#fff" stroke-width="1.5"/>
    </svg>
    <div class="footer-bar"></div><span class="page-num">8</span>
  </section>

  <!-- 8 Quote -->
  <section class="slide c2 r3">
    <div class="brand-tag"><i></i>Velmora</div>
    <div class="quote-band"></div>
    <div class="quote-frame"></div>
    <p class="quote-text">&ldquo;This is a quote. Words full of wisdom that someone important said and can make the reader get inspired.&rdquo;</p>
    <div class="quote-cite">&mdash;SOMEONE FAMOUS</div>
    <div class="footer-bar"></div><span class="page-num">9</span>
  </section>

  <!-- 9 Photo with points -->
  <section class="slide c3 r3">
    <div class="brand-tag"><i></i>Velmora</div>
    <div class="abs" style="left:0;right:0;top:143px;bottom:0;background:var(--blue)"></div>
    <div class="placeholder" style="left:14px;top:17px;width:140px;height:177px;background:linear-gradient(150deg,#d9c4ad,#b08d73 45%,#e6e6ea 70%,#d33 100%)" role="img" aria-label="Photo of hands signing a contract beside a red toy car"></div>
    <div class="round-icon abs" style="left:169px;top:41px;width:28px;height:28px;background:var(--blue)"><svg width="13" height="13" viewBox="0 0 13 13"><rect x="1" y="1" width="11" height="11" fill="none" stroke="#fff"/><path d="M3.5 10V7M6.5 10V5M9.5 10V3" stroke="#fff" stroke-width="1.4"/></svg></div>
    <div class="round-icon abs" style="left:169px;top:88px;width:28px;height:28px;background:var(--yellow)"><svg width="13" height="13" viewBox="0 0 13 13"><rect x="2.5" y="1" width="8" height="11" fill="none" stroke="#fff"/><path d="M4 4h5M4 7h5M4 10h5" stroke="#fff"/></svg></div>
    <p class="abs body-text" style="left:204px;top:50px;width:160px;font-size:4.4px"><span class="small-head">Lorem ipsum dolor</span><br>Lorem ipsum dolor sit amet, consectetur adipiscing elit, sed do eiusmod tempor incididunt ut labore et dolore magna aliqua. Ut enim ad minim veniam, quis nostrud exercitation ullamco laboris nisi ut.</p>
    <p class="abs body-text" style="left:204px;top:97px;width:160px;font-size:4.4px"><span class="small-head">Lorem ipsum dolor</span><br>Lorem ipsum dolor sit amet, consectetur adipiscing elit, sed do eiusmod tempor incididunt ut labore et dolore magna aliqua. Ut enim ad minim veniam, quis nostrud exercitation ullamco laboris nisi ut.</p>
    <p class="abs body-text" style="left:168px;top:156px;width:190px;color:#fff;font-size:4.8px">Lorem ipsum dolor sit amet, consectetur adipiscing elit, sed do eiusmod tempor incididunt ut labore et dolore magna aliqua. Ut enim ad minim veniam, quis nostrud exercitation ullamco laboris nisi ut aliquip ex</p>
    <span class="page-num" style="bottom:2px">10</span>
  </section>

  <!-- 10 Photo statement -->
  <section class="slide c1 r4">
    <div class="photo-fill" style="background:linear-gradient(165deg,#9a4a3e,#6e5050 30%,#c98a4a 55%,#3a3a40 80%)" role="img" aria-label="Photo of a car dealership lot with rows of vehicles in sunlight"></div>
    <div class="abs" style="left:0;right:0;top:129px;bottom:0;background:rgba(30,30,30,.55)"></div>
    <p class="abs" style="left:15px;top:144px;width:350px;font-size:8.8px;line-height:1.5;font-weight:700;color:#fff">Sed ut perspiciatis, unde omnis iste natus error sit voluptatem accusantium doloremque laudantium, totam rem aperiam eaque ipsa, quae ab illo inventore veritatis et quasi architecto beatae vitae dicta sunt, explicabo. Nemo enim ipsam voluptatem, quia voluptas sit.</p>
    <span class="page-num" style="bottom:2px">11</span>
  </section>

  <!-- 11 Chart -->
  <section class="slide c2 r4">
    <div class="slide-title" style="left:108px;top:20px">Lorem ipsum dolor eta</div>
    <div class="brand-tag"><i></i>Velmora</div>
    <svg class="abs" style="left:30px;top:60px" width="140" height="95" viewBox="0 0 140 95">
      <g font-family="Open Sans, sans-serif" font-size="4" text-anchor="middle">
        <rect x="9.5" y="19" width="11" height="64" fill="#3a99d2"/>
        <rect x="9" y="9" width="12" height="6" fill="#e5e5e5"/><text x="15" y="13.5" font-weight="700">80</text>
        <rect x="42.5" y="55" width="11" height="28" fill="#c9a45a"/>
        <rect x="42" y="45" width="12" height="6" fill="#e5e5e5"/><text x="48" y="49.5" font-weight="700">35</text>
        <rect x="74.5" y="39" width="11" height="44" fill="#fcc95b"/>
        <rect x="74" y="29" width="12" height="6" fill="#e5e5e5"/><text x="80" y="33.5" font-weight="700">55</text>
        <rect x="106.5" y="75" width="11" height="8" fill="#4b4b4b"/>
        <rect x="106" y="65" width="12" height="6" fill="#e5e5e5"/><text x="112" y="69.5" font-weight="700">10</text>
        <path d="M0 83.5h130" stroke="#ccc" stroke-width=".5"/>
        <text x="15" y="90" font-size="3">Category 1</text><text x="48" y="90" font-size="3">Category 2</text>
        <text x="80" y="90" font-size="3">Category 3</text><text x="112" y="90" font-size="3">Category 4</text>
      </g>
    </svg>
    <div class="info-strip">
      <div class="round-icon" style="background:var(--blue)"><svg width="9" height="9" viewBox="0 0 9 9"><circle cx="4.5" cy="4.5" r="3.5" fill="none" stroke="#fff"/><circle cx="4.5" cy="4.5" r="1.3" fill="#fff"/></svg></div>
      <p><b>Lorem ipsum dolor</b><br>Sed ut perspiciatis, unde omnis iste natus error sit voluptatem accusantium doloremque laudantium.</p>
      <div class="round-icon" style="background:var(--yellow)"><svg width="9" height="9" viewBox="0 0 9 9"><rect x="1" y="2" width="7" height="5" fill="none" stroke="#fff"/></svg></div>
      <p><b>Lorem ipsum dolor</b><br>Sed ut perspiciatis, unde omnis iste natus error sit voluptatem accusantium doloremque laudantium.</p>
    </div>
    <div class="stat-circle"><strong>$1.3</strong><span>Million Raising</span></div>
    <div class="footer-bar"></div><span class="page-num">12</span>
  </section>

  <!-- 12 Contact -->
  <section class="slide c3 r4">
    <div class="brand-tag"><i></i>Velmora</div>
    <div class="contact-bubble">
      <h3>Get in Touch</h3>
      <p>Lorem ipsum dolor sit amet, consectetur adipiscing elit, sed do eiusmod tempor incididunt ut labore et dolore magna aliqua. Ut enim ad minim veniam, quis nostrud exercitation ullamco laboris nisi ut aliquip ex ea commodo consequat.</p>
    </div>
    <svg class="contact-tail" width="24" height="28" viewBox="0 0 24 28"><path d="M0 0L22 14L0 28z" fill="#4b4b4b"/></svg>
    <div class="person-name">Marcus Ellery</div>
    <div class="person-role">IT Director</div>
    <div class="contact-line" style="top:84px"><span class="round-icon"><svg width="9" height="9" viewBox="0 0 9 9"><path d="M2 1l1.5 2-1 1c.6 1.3 1.3 2 2.5 2.5l1-1 2 1.5-1 1.5C4 8.5.5 5 .5 2z" fill="#3a99d2"/></svg></span>Mobile: 08 41 27 63 18</div>
    <div class="contact-line" style="top:116px"><span class="round-icon"><svg width="10" height="8" viewBox="0 0 10 8"><rect width="10" height="8" rx="1" fill="#3a99d2"/><path d="M0 1l5 3.5L10 1" stroke="#fff" fill="none" stroke-width=".8"/></svg></span>Email: office@velmora.com</div>
    <div class="contact-line" style="top:149px"><span class="round-icon"><svg width="10" height="10" viewBox="0 0 10 10" fill="none" stroke="#3a99d2" stroke-width=".8"><circle cx="5" cy="5" r="4.2"/><ellipse cx="5" cy="5" rx="1.8" ry="4.2"/><path d="M.8 5h8.4M1.5 3h7M1.5 7h7"/></svg></span>WWW.VELMORA.COM</div>
    <div class="tagline">The ultimate insurance comparison</div>
    <div class="footer-bar"></div><span class="page-num">13</span>
  </section>

</main>
</body>
</html>
```